Caldrow Supplies Business Card

Professional business card that stand out to our potential customers. Front and back with clean modern design

Industry/Entity Type

Oil and gas

Contact Information for Business Card

Name, address, website , office phone and cell number

Requirements
Must have
• Editable files for each employee

```html
<!DOCTYPE html>
<html lang="en">
<head>
<meta charset="UTF-8">
<title>Caldrow Supplies Business Card</title>
<link href="https://fonts.googleapis.com/css2?family=Poppins:wght@400;500;700;800&display=swap" rel="stylesheet">
<style>
  :root {
    --stage: #3a3a3a;
    --card-white: #ffffff;
    --card-black: #141414;
    --brand-red: #e31e24;
    --brand-blue: #1fa9cf;
    --ink: #222222;
    --muted: #555555;
  }
  * { margin: 0; padding: 0; box-sizing: border-box; }
  html, body { width: 1200px; height: 875px; overflow: hidden; }
  body {
    background: var(--stage);
    font-family: "Poppins", sans-serif;
    position: relative;
  }
  .card {
    position: absolute;
    top: 283px;
    width: 540px;
    height: 309px;
    border-radius: 18px;
    overflow: hidden;
  }
  /* Back side */
  .card-back { left: 40px; background: var(--card-black); }
  .back-pattern {
    position: absolute; inset: 0;
    background: linear-gradient(100deg, #8a8a8a 0%, #4a4a4a 30%, #222 60%, #0d0d0d 100%);
    opacity: .55;
  }
  .back-brand {
    position: absolute; left: 50%; top: 50%;
    transform: translate(-50%, -50%);
    display: flex; align-items: center; gap: 10px;
    background: var(--card-black);
    padding: 10px 18px; border-radius: 6px;
  }
  .back-brand .mark { width: 14px; height: 14px; background: var(--brand-red); }
  .back-brand .name {
    color: #ffffff; font-weight: 700; font-size: 20px; letter-spacing: .5px;
  }
  /* Front side */
  .card-front { left: 620px; background: var(--card-white); }
  .front-brand {
    position: absolute; right: 34px; top: 52px;
    display: flex; align-items: center; gap: 10px;
  }
  .front-brand .mark { width: 16px; height: 16px; background: var(--brand-red); }
  .front-brand .name {
    color: var(--brand-red); font-weight: 800; font-size: 24px;
    text-transform: uppercase; letter-spacing: .5px;
  }
  .divider-line {
    position: absolute; right: 34px; top: 112px;
    width: 300px; height: 1.5px; background: var(--brand-red);
  }
  .address {
    position: absolute; right: 34px; top: 124px;
    text-align: right; font-size: 12.5px; line-height: 1.35; color: var(--ink);
  }
  .person { position: absolute; left: 30px; top: 160px; }
  .person-name { color: var(--brand-red); font-weight: 700; font-size: 24px; line-height: 1.1; }
  .person-title { font-size: 13px; color: var(--ink); margin-top: 2px; }
  .person-rule { width: 210px; height: 1.5px; background: var(--brand-red); margin-top: 3px; }
  .contacts { list-style: none; margin-top: 6px; }
  .contacts li {
    display: flex; align-items: center; gap: 7px;
    font-size: 12.5px; line-height: 1.35; color: var(--ink);
  }
  .contacts svg { width: 10px; height: 10px; fill: var(--brand-red); flex: none; }
  .band-red {
    position: absolute; left: 0; bottom: 0; width: 78%; height: 14px;
    background: var(--brand-red);
  }
  .band-blue {
    position: absolute; right: 0; bottom: 0; width: 22%; height: 14px;
    background: var(--brand-blue);
  }
</style>
</head>
<body>

<section class="card card-back" aria-label="Card back">
  <div class="back-pattern" role="img" aria-label="Repeating brand pattern in silver to black gloss"></div>
  <div class="back-brand">
    <span class="mark"></span>
    <span class="name">Caldrow Supplies</span>
  </div>
</section>

<section class="card card-front" aria-label="Card front">
  <div class="front-brand">
    <span class="mark"></span>
    <span class="name">Caldrow Supplies</span>
  </div>
  <div class="divider-line"></div>
  <p class="address">412 W.Harlow Suite 2<br>Basinview, Tx 70412</p>

  <div class="person">
    <h1 class="person-name">Marcus Hale</h1>
    <p class="person-title">President</p>
    <div class="person-rule"></div>
    <ul class="contacts">
      <li><svg viewBox="0 0 10 10"><path d="M2 0.5 L3.8 2.6 L2.9 3.7 Q4 6 6.3 7.1 L7.4 6.2 L9.5 8 L8.3 9.5 Q1 8.5 0.5 1.7 Z"/></svg>(555)014-2276</li>
      <li><svg viewBox="0 0 10 10"><path d="M2.5 0 H7.5 V10 H2.5 Z M3.3 1 V8 H6.7 V1 Z"/></svg>(555)014-2276</li>
      <li><svg viewBox="0 0 10 10"><path d="M0 2 H10 V8.5 H0 Z M0.8 2.6 L5 5.6 L9.2 2.6 Z"/></svg>sales@caldrowsupplies.com</li>
      <li><svg viewBox="0 0 10 10"><circle cx="5" cy="5" r="4.5"/></svg>www.caldrowsupplies.com</li>
    </ul>
  </div>

  <div class="band-red"></div>
  <div class="band-blue"></div>
</section>

</body>
</html>
```